Golden Meadow Kit Social Media Graphics

Focusing on the Golden Meadow Kit product (3 product bundle), create 6-7 individual social media graphics (square size). For the color scheme of the graphics, they should all be complementary with the Golden Meadow Kit bottle colors.

Note: each graphic should have one of the pictures of the bottles (3-product bundle) on it and/or one of the images with a person on it (several pics attached to choose from). I even included some real customer “before and afters” pictures…you can use them if you think the quality is good enough.

Target Market(s)

men and women looking for fast, healthy loss

Industry/Entity Type

health and wellness

Requirements
Must have
• the product is a picture of ALL 3 bottles; no single bottles will be selected

```html
<!DOCTYPE html>
<html lang="en">
<head>
<meta charset="utf-8">
<title>Golden Meadow Kit – Social Graphics</title>
<link href="https://fonts.googleapis.com/css2?family=Figtree:ital,wght@0,600;0,700;0,800;1,800&display=swap" rel="stylesheet">
<style>
  :root{
    --board:#ffffff;
    --label:#9a9a9a;
    --white:#ffffff;
    --gold:#f7d36b;
    --ink:#1b1530;
    --red:#9c161f;
    --red-line:#e4262f;
    --purple-deep:#5a1d91;
  }
  *{box-sizing:border-box;margin:0;padding:0}
  html,body{width:1200px;height:753px;overflow:hidden;background:var(--board);font-family:"Figtree",sans-serif}
  .board{position:relative;width:1200px;height:753px}
  .panel-label{position:absolute;top:115px;font-size:21px;font-weight:700;color:var(--label);letter-spacing:-.3px}
  .graphic{position:absolute;top:186px;width:459px;height:459px;overflow:hidden}
  .graphic-inner{position:absolute;left:0;top:0;width:530px;height:530px;transform:scale(.866);transform-origin:0 0}
  .graphic-inner svg{position:absolute;left:0;top:0}
  .headline-burn{position:absolute;left:40px;top:34px;font-size:49px;font-weight:800;line-height:46px;color:var(--white);letter-spacing:-1px}
  .headline-burn .gold{color:var(--gold)}
  .subline-burn{position:absolute;left:40px;top:138px;font-size:26px;font-weight:700;line-height:32px;color:var(--white);letter-spacing:-.4px}
  .headline-trio{position:absolute;left:0;right:0;top:28px;text-align:center;font-size:39px;font-weight:800;line-height:50px;color:var(--white);letter-spacing:-.8px}
  .headline-trio em{color:var(--ink);font-style:italic}
  .result-card{position:absolute;top:145px;width:141px;height:141px;border:3px solid var(--white);border-radius:16px;overflow:hidden;display:flex}
  .result-photo{flex:1}
  .result-photo.before{background:linear-gradient(180deg,#6b6a70,#2c2a30)}
  .result-photo.after{background:linear-gradient(180deg,#8a8690,#3a3640)}
  .result-tags{position:absolute;left:0;right:0;bottom:8px;display:flex;justify-content:space-around;font-size:12.5px;font-weight:800;color:var(--white)}
</style>
</head>
<body>
<div class="board">
  <div class="panel-label" style="left:125px">Image 1</div>
  <div class="panel-label" style="left:616px">Image 2</div>

  <section class="graphic" style="left:125px">
    <div class="graphic-inner">
      <svg width="530" height="530" viewBox="0 0 530 530">
        <defs>
          <linearGradient id="bgBurn" x1="0" y1="1" x2="1" y2="0">
            <stop offset="0" stop-color="#6b3fb0"/>
            <stop offset=".55" stop-color="#b274c9"/>
            <stop offset="1" stop-color="#e2506e"/>
          </linearGradient>
          <linearGradient id="modelBurn" x1="0" y1="0" x2="0" y2="1">
            <stop offset="0" stop-color="#eea3bb"/>
            <stop offset="1" stop-color="#d9809f"/>
          </linearGradient>
          <linearGradient id="redCircle" x1="0" y1="0" x2="1" y2="1">
            <stop offset="0" stop-color="#86121b"/>
            <stop offset="1" stop-color="#b01c25"/>
          </linearGradient>
          <linearGradient id="bottleFill" x1="0" y1="0" x2="1" y2="0">
            <stop offset="0" stop-color="#d9dce6"/>
            <stop offset=".5" stop-color="#ffffff"/>
            <stop offset="1" stop-color="#cfd3de"/>
          </linearGradient>
        </defs>
        <rect width="530" height="530" fill="url(#bgBurn)"/>
        <path d="M270 0 H500 Q530 200 470 530 H300 Q240 300 270 0 Z" fill="url(#modelBurn)" role="img" aria-label="Photo of a woman in pink activewear resting hands on her hips"/>
        <path d="M0 420 Q120 400 200 430 Q240 450 260 530 L0 530 Z" fill="var(--purple-deep)" opacity=".8"/>
        <path d="M330 530 A240 240 0 0 0 300 400" fill="none" stroke="#5c1f95" stroke-width="3"/>
        <path d="M0 395 A120 120 0 0 1 40 370" fill="none" stroke="#5c1f95" stroke-width="3"/>
        <circle cx="105" cy="0" r="272" fill="url(#redCircle)"/>
        <path d="M376 0 A288 288 0 0 1 190 288" fill="none" stroke="var(--red-line)" stroke-width="3"/>
        <path d="M0 255 Q80 283 180 285" fill="none" stroke="var(--red-line)" stroke-width="3"/>
        <g role="img" aria-label="Golden Meadow Kit three-bottle bundle: Glucose Balance, Liver Renew and Belly Ease">
          <rect x="25" y="312" width="85" height="185" rx="12" fill="url(#bottleFill)"/>
          <rect x="113" y="300" width="105" height="197" rx="12" fill="url(#bottleFill)"/>
          <rect x="223" y="312" width="95" height="185" rx="12" fill="url(#bottleFill)"/>
        </g>
      </svg>
      <h2 class="headline-burn">Burn <span class="gold">Belly</span><br><span class="gold">Fat</span> Fast</h2>
      <p class="subline-burn">The 3-Part Solution<br>You Need Now!</p>
    </div>
  </section>

  <section class="graphic" style="left:616px">
    <div class="graphic-inner">
      <svg width="530" height="530" viewBox="0 0 530 530">
        <defs>
          <linearGradient id="bgTrio" x1="0" y1="0" x2="1" y2="0">
            <stop offset="0" stop-color="#a978d0"/>
            <stop offset="1" stop-color="#e0527a"/>
          </linearGradient>
          <linearGradient id="bottleFill2" x1="0" y1="0" x2="1" y2="0">
            <stop offset="0" stop-color="#d9dce6"/>
            <stop offset=".5" stop-color="#ffffff"/>
            <stop offset="1" stop-color="#cfd3de"/>
          </linearGradient>
        </defs>
        <rect width="530" height="530" fill="url(#bgTrio)"/>
        <path d="M90 530 A175 175 0 0 1 440 530 Z" fill="var(--purple-deep)" opacity=".9"/>
        <path d="M20 530 A200 200 0 0 1 90 420" fill="none" stroke="var(--purple-deep)" stroke-width="3"/>
        <path d="M35 530 A190 190 0 0 1 100 430" fill="none" stroke="var(--purple-deep)" stroke-width="3"/>
        <path d="M460 530 A220 220 0 0 0 510 430" fill="none" stroke="var(--purple-deep)" stroke-width="3"/>
        <path d="M57 302 Q52 345 92 364" fill="none" stroke="var(--white)" stroke-width="3" stroke-linecap="round"/>
        <path d="M80 352 L94 365 L78 372" fill="none" stroke="var(--white)" stroke-width="3" stroke-linecap="round" stroke-linejoin="round"/>
        <path d="M463 302 Q468 345 428 364" fill="none" stroke="var(--white)" stroke-width="3" stroke-linecap="round"/>
        <path d="M440 352 L426 365 L442 372" fill="none" stroke="var(--white)" stroke-width="3" stroke-linecap="round" stroke-linejoin="round"/>
        <g role="img" aria-label="Golden Meadow Kit three-bottle bundle: Glucose Balance, Liver Renew and Belly Ease">
          <rect x="118" y="312" width="85" height="185" rx="12" fill="url(#bottleFill2)"/>
          <rect x="206" y="300" width="105" height="197" rx="12" fill="url(#bottleFill2)"/>
          <rect x="316" y="312" width="95" height="185" rx="12" fill="url(#bottleFill2)"/>
        </g>
      </svg>
      <h2 class="headline-trio">Double Your <em>Weight Loss</em><br>With this Powerful Trio!</h2>

      <div class="result-card" style="left:32px">
        <div class="result-photo before" role="img" aria-label="Customer before photo"></div>
        <div class="result-photo after" role="img" aria-label="Customer after photo"></div>
        <div class="result-tags"><span>BEFORE</span><span>AFTER</span></div>
      </div>
      <div class="result-card" style="left:195px">
        <div class="result-photo before" style="background:linear-gradient(180deg,#7d8a70,#3e4838)" role="img" aria-label="Customer before photo"></div>
        <div class="result-photo after" style="background:linear-gradient(180deg,#8e9a88,#4a5046)" role="img" aria-label="Customer after photo"></div>
        <div class="result-tags"><span>BEFORE</span><span>AFTER</span></div>
      </div>
      <div class="result-card" style="left:358px">
        <div class="result-photo before" style="background:linear-gradient(180deg,#5e5e66,#2a2a30)" role="img" aria-label="Customer before photo"></div>
        <div class="result-photo after" style="background:linear-gradient(180deg,#6e6a60,#2e2c2a)" role="img" aria-label="Customer after photo"></div>
        <div class="result-tags"><span>BEFORE</span><span>AFTER</span></div>
      </div>
    </div>
  </section>
</div>
</body>
</html>
```